Stationary Set and Logo Update **PAYMENT GUARANTEED**

Stationery Design and Logo Update

About Us

Trindex Supply is a wholesale distributor of OEM [original brand] and compatible [generic brand] parts and supplies for use in copiers, faxes, printers, and multi-function machines. In plain English…we sell all the parts and supplies [such as toner] that make up any office equipment which outputs an image on paper.

Trindex was the 1st distributor to develop and sell a generic brand copier part in the United States. We have been in business since 1972 [nearly 40 years]. Our tagline is "The Steady Choice," as in our company was the first alternative product that copier dealers had to buying original brand copier parts. Trindex is known for offering reliable and cost-effective OEM and compatible products.

Project

We require a fresh, modern and corporate identity. Please submit a stationary package inclusive of a double-sided business card (2" x 3.5"), letterhead (8.5'x11"), and standard #10 envelope (4-1/8” x 9-1/2). You may use our current logo or preferably your take on an updated one. If an attempt is made in updating the logo #004D8E or a similar hue should be used as the primary color.

The design should be clean, simple, modern and professional and make an immediate impact.

Target Market(s)

Copier and printer dealers who lease and service imaging equipment in the United States and Latin America.

Industry/Entity Type

Business

Requirements
Must have
• Simple, clean, modern and professional. Please use #004D8E or a similar hue as the primary color. Letterhead must accommate (2) addresses. We have 2 locations.
Nice to have
• A simple, modern update to our current logo. https://assets.mailvorbo.example/fs030/5520384417702/img/418.jpg
Should not have
• More than (2) colors on logo.

```html
<!DOCTYPE html>
<html lang="en">
<head>
<meta charset="utf-8">
<title>Trindex Supply Stationery</title>
<link href="https://fonts.googleapis.com/css2?family=Jost:wght@400&display=swap" rel="stylesheet">
<style>
  :root {
    --brand-blue: #004D8E;
    --ink: #2e2e2e;
    --paper: #ffffff;
    --backdrop: #ffffff;
    --accent-tint: #ececec;
    --shadow: rgba(0,0,0,0.45);
  }
  html, body {
    margin: 0; padding: 0;
    width: 1200px; height: 900px;
    overflow: hidden;
    background: var(--backdrop);
    font-family: "Jost", "Futura", sans-serif;
    color: var(--ink);
  }
  .board { position: relative; width: 1200px; height: 900px; }
  .sheet {
    position: absolute;
    background: var(--paper);
    box-shadow: 3px 4px 5px var(--shadow);
    overflow: hidden;
  }
  .accent-circle {
    position: absolute;
    border-radius: 50%;
    background: var(--accent-tint);
  }
  .wordmark {
    position: absolute;
    color: var(--brand-blue);
    font-weight: 400;
    line-height: 1;
    white-space: nowrap;
  }

  /* Letterhead */
  .letterhead { left: 20px; top: 55px; width: 610px; height: 790px; }
  .letterhead .wordmark { left: 16px; top: 28px; font-size: 40px; }
  .letterhead .accent-circle { left: 60px; top: 200px; width: 400px; height: 400px; }
  .address {
    position: absolute;
    font-size: 10.5px;
    line-height: 13.2px;
  }
  .letterhead .address-main { left: 19px; top: 696px; }
  .letterhead .address-west { right: 19px; top: 696px; text-align: right; }
  .contact-line {
    position: absolute;
    left: 0; right: 0;
    text-align: center;
  }
  .web { color: var(--brand-blue); }
  .letterhead .web { top: 739px; font-size: 13px; }
  .letterhead .tollfree { top: 760px; font-size: 14.5px; }

  /* Envelope */
  .envelope { left: 498px; top: 80px; width: 686px; height: 296px; }
  .envelope .accent-circle { left: 360px; top: 20px; width: 270px; height: 270px; }
  .envelope .wordmark { left: 22px; top: 232px; font-size: 38px; }

  /* Business card front */
  .card-front { left: 700px; top: 473px; width: 252px; height: 144px; }
  .card-front .wordmark { left: 0; right: 0; text-align: center; top: 46px; font-size: 46px; }

  /* Business card back */
  .card-back { left: 893px; top: 597px; width: 262px; height: 144px; }
  .card-back .accent-circle { left: 62px; top: 22px; width: 110px; height: 110px; }
  .card-back .web { top: 38px; font-size: 11px; }
  .card-back .tollfree { top: 55px; font-size: 12px; }
  .card-back .address { font-size: 7px; line-height: 9.2px; top: 89px; }
  .card-back .address-main { left: 9px; }
  .card-back .address-west { right: 9px; text-align: right; }
</style>
</head>
<body>
<main class="board">

  <section class="sheet letterhead" aria-label="Letterhead">
    <div class="accent-circle"></div>
    <div class="wordmark">Trindex</div>
    <div class="address address-main">
      Trindex Supply<br>Corporate Office<br>2250 Harbor Ridge Road<br>Port Alden, FL 33990<br>Local: 555.210.4400<br>Fax: 555.210.4411
    </div>
    <div class="contact-line web">www.trindexsupply.example</div>
    <div class="contact-line tollfree">Toll Free: 800.555.0142</div>
    <div class="address address-west">
      Trindex West<br>West Coast Fulfillment Center<br>North Basin Business Park #7<br>4720 Larkspur Lane Carver,<br>NV 89777<br>Fax: 555.384.9120
    </div>
  </section>

  <section class="sheet envelope" aria-label="Envelope">
    <div class="accent-circle"></div>
    <div class="wordmark">Trindex</div>
  </section>

  <section class="sheet card-front" aria-label="Business card front">
    <div class="wordmark">Trindex</div>
  </section>

  <section class="sheet card-back" aria-label="Business card back">
    <div class="accent-circle"></div>
    <div class="contact-line web">www.trindexsupply.example</div>
    <div class="contact-line tollfree">Toll Free: 800.555.0142</div>
    <div class="address address-main">
      Trindex Supply<br>Corporate Office<br>2250 Harbor Ridge Road<br>Port Alden, FL 33990<br>Local: 555.210.4400<br>Fax: 555.210.4411
    </div>
    <div class="address address-west">
      Trindex West<br>West Coast Fulfillment Center<br>North Basin Business Park #7<br>4720 Larkspur Lane Carver,<br>NV 89777<br>Fax: 555.384.9120
    </div>
  </section>

</main>
</body>
</html>
```